Marlow Realty Real Estate Brokerage Recruiting Flyer

We are a real estate brokerage looking to hire more real estate agents. We need to list everything we have to offer as a company so real estate agents will join our company. this is our company website: www.Marlowrealty.example .

100% COMMISSION NO MONTHLY FEE
$450 Flat Transaction FEE

What We Offer:
24/7 Office Access
Free E & O Insurance for 1st Year
Free Online CE and PLE
Free 1,000 Business Cards
Free Professional Social Media Marketing
Free Printing, Scanning, and Copies
Free Buyer and Seller Presentation Packages
Free Filquay Cloud Based Document Management Access
Access to our Internal Brokerage Forum
Company Profit Sharing!
Private Offices Available to Rent

*Lead Generation Software with over 3,000 Leads
*10 Leads to Start
* Free Personal CRM and Website
*Restrictions and Rules apply

Company Address:
4817 Amberfield Road
Suite 512
Fairfax, VA 22194
Phone: 703-555-0147
email: info@marlowrealty.example

Target Market(s)

Real Estate Agents

Industry/Entity Type

Real Estate

Colors
0555a3
ffffff

Requirements
Must have
• 100% COMMISSION NO MONTHLY FEE
$450 Flat Transaction FEE

What We Offer:
24/7 Office Access
Free Online CE and PLE
Free 1,000 Business Cards
Company Profit Sharing!

*10 Leads to Start

Company Address:
4817 Amberfield Road
Suite 512
Fairfax, VA 22194
Phone: 703-555-0147

```html
<!DOCTYPE html>
<html lang="en">
<head>
<meta charset="utf-8">
<title>Marlow Realty – Agent Recruiting Flyer</title>
<link rel="stylesheet" href="https://fonts.googleapis.com/css2?family=Montserrat:wght@300;500;600;700;800;900&family=Oswald:wght@500&display=swap">
<style>
:root{
  --brand-blue:#0a3a7e;
  --accent-blue:#0555a3;
  --ink:#4a4a4a;
  --charcoal:#3a3a3a;
  --paper:#ffffff;
  --backdrop:#e6e7ea;
}
*{box-sizing:border-box;margin:0;padding:0}
html,body{width:1200px;height:800px;overflow:hidden;background:var(--backdrop)}
body{position:relative;font-family:"Montserrat",sans-serif;color:var(--ink)}
.flyer{position:absolute;left:320px;top:38px;width:560px;height:724px;background:var(--paper);overflow:hidden;box-shadow:0 4px 18px rgba(0,0,0,.18)}
.brand{position:absolute;left:26px;top:24px;display:flex;align-items:center;gap:8px}
.brand__mark{width:18px;height:18px;background:var(--brand-blue)}
.brand__name{font-weight:600;font-size:19px;color:var(--brand-blue);letter-spacing:.5px}
.headline{position:absolute;left:236px;top:14px;line-height:1}
.headline__main{font-weight:900;font-size:25px;color:var(--brand-blue)}
.headline__sub{font-weight:300;font-size:25px;color:var(--charcoal);letter-spacing:1px;margin-top:2px}
.frame-top{position:absolute;left:500px;top:20px;width:50px;height:9px;background:var(--brand-blue)}
.frame-side{position:absolute;left:540px;top:20px;width:10px;height:300px;background:var(--brand-blue)}
.photo{position:absolute}
.photo--house{left:22px;top:66px;width:518px;height:244px;background:linear-gradient(180deg,#e9edf1 0%,#8a8478 45%,#6f7a5a 80%,#5f7a3e 100%)}
.blue-band{position:absolute;left:0;top:290px;width:560px;height:112px;background:var(--brand-blue)}
.blue-band--left{position:absolute;left:0;top:395px;width:312px;height:50px;background:var(--brand-blue)}
.photo--hands{left:38px;top:246px;width:252px;height:150px;border:5px solid var(--paper);background:linear-gradient(135deg,#dfeccf,#c9b39d 55%,#eef3e6)}
.photo--agent{left:304px;top:282px;width:246px;height:124px;border:5px solid var(--paper);border-bottom:0;background:linear-gradient(135deg,#f3d79a,#b7a592 50%,#7f8f66)}
.fee{position:absolute;left:38px;top:404px;font-family:"Oswald",sans-serif;font-weight:500;font-size:21px;line-height:30px;color:var(--paper);letter-spacing:.2px;white-space:nowrap}
.offer-title{position:absolute;left:40px;top:450px;font-weight:900;font-size:26px;line-height:30px;color:var(--ink);letter-spacing:.5px}
.offer-title::after{content:"";display:block;width:88px;height:5px;background:var(--brand-blue);margin-top:2px}
.checklist{position:absolute;list-style:none;font-size:11px;font-weight:600;color:var(--ink)}
.checklist li{display:flex;align-items:flex-start;gap:8px;line-height:1.3;margin-bottom:4px}
.checklist svg{flex:none;width:11px;height:11px;margin-top:1px;color:var(--accent-blue)}
.checklist--left{left:44px;top:494px}
.checklist--right{left:312px;top:418px;width:236px}
.perks-band{position:absolute;left:0;top:602px;width:560px;height:62px;background:linear-gradient(90deg,var(--charcoal),#555 60%,var(--charcoal));display:flex;align-items:center}
.perks-col{list-style:none;font-size:11px;font-weight:600;color:var(--paper);padding:0 40px;flex:1}
.perks-col li{display:flex;gap:8px;align-items:flex-start;margin:4px 0;line-height:1.25}
.perks-col svg{flex:none;width:11px;height:11px;margin-top:1px}
.perks-divider{width:0;height:40px;border-left:2px dotted #bbb}
.contact{position:absolute;left:0;top:664px;width:560px;height:60px;display:flex;align-items:center;justify-content:space-around;font-size:11px;font-weight:600;color:var(--ink)}
.contact__item{display:flex;align-items:center;gap:7px;line-height:1.25}
.contact__item svg{width:16px;height:16px;flex:none}
.contact__rule{width:1px;height:30px;background:#999}
</style>
</head>
<body>
<svg width="0" height="0" style="position:absolute">
  <symbol id="tick" viewBox="0 0 12 12"><circle cx="6" cy="6" r="5" fill="none" stroke="currentColor" stroke-width="1.2"/><path d="M3.5 6.2l1.7 1.7 3.3-3.6" fill="none" stroke="currentColor" stroke-width="1.3"/></symbol>
</svg>
<main class="flyer">
  <div class="brand"><span class="brand__mark"></span><span class="brand__name">Marlow Realty</span></div>
  <h1 class="headline"><div class="headline__main">100% COMMISSION</div><div class="headline__sub">NO MONTHLY FEE</div></h1>
  <div class="frame-top"></div>
  <div class="frame-side"></div>
  <div class="photo photo--house" role="img" aria-label="Photo of a large two-storey suburban house with front lawn and trees"></div>
  <div class="blue-band"></div>
  <div class="blue-band--left"></div>
  <div class="photo photo--hands" role="img" aria-label="Photo of cupped hands holding a small model house"></div>
  <div class="photo photo--agent" role="img" aria-label="Photo of an agent greeting a couple outside an open house"></div>
  <p class="fee">$450 FLAT TRANSACTION FEE</p>
  <h2 class="offer-title">WHAT WE OFFER</h2>
  <ul class="checklist checklist--left">
    <li><svg><use href="#tick"/></svg>24/7 Office Access</li>
    <li><svg><use href="#tick"/></svg>Free E &amp; O Insurance for 1st Year</li>
    <li><svg><use href="#tick"/></svg>Free Online CE and PLE</li>
    <li><svg><use href="#tick"/></svg>Free 1,000 Business Cards</li>
    <li><svg><use href="#tick"/></svg>Free Professional Social Media Marketing</li>
    <li><svg><use href="#tick"/></svg>Free Printing, Scanning, and Copies</li>
  </ul>
  <ul class="checklist checklist--right">
    <li><svg><use href="#tick"/></svg>Free Buyer and Seller Presentation Packages</li>
    <li><svg><use href="#tick"/></svg>Free Filquay Cloud Based Document Management Access</li>
    <li><svg><use href="#tick"/></svg>Access to our Internal Brokerage Forum</li>
    <li><svg><use href="#tick"/></svg>Company Profit Sharing!</li>
    <li><svg><use href="#tick"/></svg>Private Offices Available to Rent</li>
  </ul>
  <section class="perks-band">
    <ul class="perks-col">
      <li><svg><use href="#tick"/></svg>Lead Generation Software with over 3,000 Leads</li>
      <li><svg><use href="#tick"/></svg>10 Leads to Start</li>
    </ul>
    <div class="perks-divider"></div>
    <ul class="perks-col">
      <li><svg><use href="#tick"/></svg>Free Personal CRM and Website</li>
      <li><svg><use href="#tick"/></svg>Restrictions and Rules apply</li>
    </ul>
  </section>
  <footer class="contact">
    <div class="contact__item">
      <svg viewBox="0 0 16 16"><path d="M3 2l3 3-1.5 2a8 8 0 0 0 4.5 4.5L11 10l3 3-2 2C6 15 1 10 1 4z" fill="var(--accent-blue)"/></svg>
      <span>703-555-0147</span>
    </div>
    <div class="contact__rule"></div>
    <div class="contact__item">
      <svg viewBox="0 0 16 16"><path d="M8 1a5 5 0 0 1 5 5c0 4-5 9-5 9S3 10 3 6a5 5 0 0 1 5-5z" fill="var(--accent-blue)"/><circle cx="8" cy="6" r="2" fill="#fff"/></svg>
      <span>4817 Amberfield Road<br>Suite 512<br>Fairfax, VA 22194</span>
    </div>
    <div class="contact__rule"></div>
    <div class="contact__item">
      <svg viewBox="0 0 16 16"><rect x="1" y="3" width="14" height="10" fill="var(--accent-blue)"/><path d="M1 3l7 6 7-6" fill="none" stroke="#fff" stroke-width="1.2"/></svg>
      <span>info@marlowrealty.example</span>
    </div>
  </footer>
</main>
</body>
</html>
```